Business Card Design Project

We are a commercial talent casting company, a very "now" company. We need a new business card that is both current, graphic and elegantly interesting. As we are a service business,
we need something that will attract the attention of new clients,
yet project a business that is 25 years old.

Industry/Entity Type

Business

Requirements
Must have
• 1. Logo - Nora Quillan Casting
2. Address - 47 Harwick Street
New York, New York 10027
3. Phone - 212-638-4170
4. E-Mail - Casting@noraquillan.com

Nice to have
• Would like the card in black and white with the only accent
color being red.

```html
<!DOCTYPE html>
<html lang="en">
<head>
<meta charset="utf-8">
<title>Nora Quillan Casting — Business Card</title>
<link rel="stylesheet" href="https://fonts.googleapis.com/css2?family=Montserrat:wght@400&display=swap">
<style>
  :root {
    --ink: #111111;
    --paper: #f2f2f2;
    --page: #ffffff;
    --accent: #e3191e;
    --rule: #dcdcdc;
    --light-text: #ffffff;
  }
  html, body {
    margin: 0;
    padding: 0;
    width: 1200px;
    height: 894px;
    overflow: hidden;
    background: var(--page);
  }
  .sheet {
    position: relative;
    width: 1200px;
    height: 894px;
    font-family: "Montserrat", sans-serif;
  }
  .card {
    position: absolute;
    top: 298px;
    width: 520px;
    height: 298px;
    border-radius: 22px;
    overflow: hidden;
    box-sizing: border-box;
  }
  .card--front {
    left: 50px;
    background: var(--paper);
    border: 1px solid var(--rule);
  }
  .card--back {
    left: 630px;
    background: var(--ink);
  }
  .edge-tab {
    position: absolute;
    left: -16px;
    width: 32px;
    height: 32px;
    border-radius: 50%;
  }
  .card--front .edge-tab { top: 128px; background: var(--ink); }
  .card--back .edge-tab { top: 70px; background: var(--accent); }

  .company-name {
    position: absolute;
    margin: 0;
    font-weight: 400;
    white-space: nowrap;
  }
  .card--front .company-name {
    left: 28px;
    top: 133px;
    font-size: 17px;
    line-height: 22px;
    color: var(--ink);
  }
  .card--back .company-name {
    left: 0;
    right: 0;
    top: 118px;
    text-align: center;
    font-size: 28px;
    line-height: 36px;
    color: var(--light-text);
  }

  .contact {
    position: absolute;
    left: 296px;
    top: 112px;
    margin: 0;
    padding: 0;
    list-style: none;
    font-size: 12px;
    line-height: 13px;
    color: var(--ink);
  }
  .contact__item {
    display: flex;
    align-items: flex-start;
    gap: 8px;
    margin-bottom: 14px;
  }
  .contact__icon {
    width: 12px;
    height: 12px;
    flex: none;
    fill: var(--accent);
  }
  .web-address {
    position: absolute;
    left: 0;
    right: 0;
    top: 214px;
    margin: 0;
    text-align: center;
    font-size: 13px;
    letter-spacing: 2.5px;
    color: var(--light-text);
  }
</style>
</head>
<body>
<main class="sheet">

  <section class="card card--front" aria-label="Card front">
    <span class="edge-tab"></span>
    <p class="company-name">Nora Quillan Casting</p>
    <ul class="contact">
      <li class="contact__item">
        <svg class="contact__icon" viewBox="0 0 12 12" aria-hidden="true">
          <path d="M6 1 L11.5 6 H10 V11 H7 V8 H5 V11 H2 V6 H0.5 Z"/>
        </svg>
        <span>47 Harwick Street<br>New York, New York 10027</span>
      </li>
      <li class="contact__item">
        <svg class="contact__icon" viewBox="0 0 12 12" aria-hidden="true">
          <path d="M2.5 1 L4.5 1 L5.2 3.6 L3.8 4.6 C4.5 6.2 5.8 7.5 7.4 8.2 L8.4 6.8 L11 7.5 L11 9.5 C11 10.3 10.3 11 9.5 11 C5 10.7 1.3 7 1 2.5 C1 1.7 1.7 1 2.5 1 Z"/>
        </svg>
        <span>212-638-4170</span>
      </li>
      <li class="contact__item">
        <svg class="contact__icon" viewBox="0 0 12 12" aria-hidden="true">
          <path d="M0.5 2.5 H11.5 V3.2 L6 6.8 L0.5 3.2 Z M0.5 4.4 L6 8 L11.5 4.4 V9.5 H0.5 Z"/>
        </svg>
        <span>Casting@noraquillan.com</span>
      </li>
    </ul>
  </section>

  <section class="card card--back" aria-label="Card back">
    <span class="edge-tab"></span>
    <p class="company-name">Nora Quillan Casting</p>
    <p class="web-address">www.noraquillan.com</p>
  </section>

</main>
</body>
</html>
```